The Wisdom of Lanterns New Book Cover Design Project

Book cover design . Paperback, ebook, and Talvora (derived from book cover) files/images required.
Book Title: The Wisdom of Lanterns
Subtitle: Under Copper Bridges
Author: Daniel Forsythe
Files: Ebook, Paperback (Brindlewick & Halvern Quill), Talvora sized image
File size & information to be provided once design is ready. Brindlewick paperback will be 5.25 x 8.
Completion date is flexible. Planning to publish in November.
Updates

Target Market(s)

Motorcycle owners

Font styles to use
Sans Serif

Requirements
Must have
• A generic looking motorcycle (samples attached). Thumbnail easily recognized as a motorcycle book.
Nice to have
• Open to all ideas but am favoring my idea: to emphasize the title lettering similar to (but not a copy of) other Wisdom books (examples attached), on a plain background. All books in the category have a motorcycle on the cover. Author name and subtitle do not have to be prominent. Rider optional..
Should not have
• Should not look like a biker romance or fantasy cover or look cartoonish. Motorcycle pic should be fairly generic (brand, style,).

```html
<!DOCTYPE html>
<html lang="en">
<head>
<meta charset="utf-8">
<title>The Wisdom of Lanterns — Cover</title>
<link rel="stylesheet" href="https://fonts.googleapis.com/css2?family=Bodoni+Moda:opsz,wght@6..96,400;6..96,500&display=swap">
<style>
  :root {
    --paper: #ffffff;
    --ink: #151515;
    --accent: #e8191c;
    --photo-dark: #0d0d0d;
    --photo-mid: #3a3a3c;
  }
  html, body {
    margin: 0;
    padding: 0;
    width: 800px;
    height: 1200px;
    overflow: hidden;
    background: var(--paper);
  }
  .cover {
    position: relative;
    width: 800px;
    height: 1200px;
    background: var(--paper);
    font-family: "Bodoni Moda", "Didot", serif;
    color: var(--ink);
  }
  .title-the {
    position: absolute;
    top: 40px;
    left: 330px;
    font-size: 170px;
    line-height: 1;
    font-weight: 500;
    margin: 0;
  }
  .title-key {
    position: absolute;
    top: 190px;
    left: 0;
    width: 800px;
    text-align: center;
    font-size: 190px;
    line-height: 1;
    color: var(--accent);
    font-weight: 400;
    letter-spacing: -2px;
  }
  .title-of {
    position: absolute;
    top: 420px;
    left: 180px;
    font-size: 90px;
    line-height: 1;
  }
  .title-subject {
    position: absolute;
    top: 510px;
    left: 0;
    width: 800px;
    text-align: center;
    font-size: 100px;
    line-height: 1;
    font-weight: 500;
  }
  .subtitle {
    position: absolute;
    top: 650px;
    left: 0;
    width: 800px;
    text-align: center;
    font-size: 22px;
    letter-spacing: 11px;
    color: var(--accent);
    text-transform: uppercase;
  }
  .cover-photo {
    position: absolute;
    top: 720px;
    left: 215px;
    width: 360px;
    height: 380px;
  }
  .author {
    position: absolute;
    top: 1105px;
    left: 0;
    width: 800px;
    text-align: center;
    font-size: 58px;
    line-height: 1;
    color: var(--accent);
    text-transform: uppercase;
    letter-spacing: 1px;
  }
</style>
</head>
<body>
  <main class="cover">
    <h1 style="margin:0;font-weight:inherit">
      <span class="title-the">The</span>
      <span class="title-key">Wisdom</span>
      <span class="title-of">of</span>
      <span class="title-subject">Lanterns</span>
    </h1>
    <p class="subtitle" style="margin:0">Under Copper Bridges</p>
    <svg class="cover-photo" viewBox="0 0 360 380" role="img" aria-label="Dark studio photograph of a generic black motorcycle, its front wheel breaking out of a circular frame">
      <defs>
        <radialGradient id="photoTone" cx="55%" cy="40%" r="65%">
          <stop offset="0%" stop-color="var(--photo-mid)"/>
          <stop offset="100%" stop-color="var(--photo-dark)"/>
        </radialGradient>
      </defs>
      <circle cx="165" cy="165" r="160" fill="url(#photoTone)"/>
      <circle cx="250" cy="285" r="92" fill="var(--photo-dark)"/>
    </svg>
    <p class="author" style="margin:0">Daniel Forsythe</p>
  </main>
</body>
</html>
```